Business Cards Design for the electrical wholesaler: clean bold dynamic :)

We need a business card design that would follow our latest brand guidelines. As an electrical wholesaler we want to bring a fresh look and feel into the industry. The design should be clean bold and dynamic. It should come alive with the renewed energy of our green colour. Our grey colour should keep things balanced and complement the notion of maturity and responsibility. We employ Lato as a corporate font however are not bound by this font and we’re open to interpretation here.

Target Market(s)

Electrical contractors

Industry/Entity Type

Business

Contact Information for Business Card

Logo
Name & Surname: Olena Dovbush
Job Title: Director of Marketing
Email: helen.dovbush@mailvane.example
Cell phone: XXX.XXX.XXXX
Address: 20917 - 87 Ave. Edmonton, AB, Canada. T6K 2R8
Business Phone: 780.555.0187
Website: www.qorvil.example

Font styles to use
Other font styles liked:
• Lato

Requirements
Must have
• Logo & website
Nice to have
• Brand elements - some of them you may find in the attached Brand Guidelines (e.g. three lines on the background signifying "W")

```html
<!DOCTYPE html>
<html lang="en">
<head>
<meta charset="utf-8">
<title>Qorvil business card</title>
<link rel="stylesheet" href="https://fonts.googleapis.com/css2?family=Lato:wght@400;700&family=Libre+Baskerville&display=swap">
<style>
  :root {
    --stage: #1b1c1e;
    --navy: #132030;
    --navy-soft: #1b2c3e;
    --gold: #b99a5b;
    --copper: #b5562a;
    --green: #8cc63f;
    --paper: #fbf9f5;
    --paper-line: #ece5da;
    --ink: #1a1a1a;
    --ink-soft: #3a3a3a;
  }
  * { box-sizing: border-box; margin: 0; padding: 0; }
  html, body { width: 1200px; height: 900px; overflow: hidden; }
  body { background: var(--stage); font-family: "Lato", sans-serif; position: relative; }

  .card {
    position: absolute;
    width: 640px;
    height: 366px;
    overflow: hidden;
    box-shadow: 0 18px 40px rgba(0,0,0,.55);
  }
  .card--front { left: 170px; top: 64px; background: var(--navy); }
  .card--back { left: 390px; top: 470px; display: flex; }

  .pattern-fill {
    position: absolute; inset: 0;
    background: linear-gradient(135deg, var(--navy) 0%, var(--navy-soft) 50%, var(--navy) 100%);
  }
  .front-frame {
    position: absolute; inset: 18px;
    border: 1.5px solid var(--gold);
  }
  .brand {
    position: absolute;
    display: flex; align-items: center; gap: 14px;
  }
  .brand__square { width: 30px; height: 30px; background: var(--green); }
  .brand__name {
    font-family: "Lato", sans-serif; font-weight: 700;
    color: var(--copper); letter-spacing: 1px; line-height: 1;
  }
  .card--front .brand { left: 50%; top: 50%; transform: translate(-50%, -50%); }
  .card--front .brand__name { font-size: 64px; }

  .back-brand-panel { position: relative; width: 45%; height: 100%; background: var(--navy); }
  .back-brand-panel .brand { left: 50%; top: 54%; transform: translate(-50%, -50%); gap: 10px; }
  .back-brand-panel .brand__name { font-size: 44px; }
  .back-brand-panel .brand__square { width: 22px; height: 22px; }

  .contact-panel {
    position: relative; width: 55%; height: 100%;
    background: linear-gradient(160deg, var(--paper) 0%, var(--paper-line) 100%);
    padding: 66px 30px 0 44px;
  }
  .contact-panel__pattern { position: absolute; inset: 0; background: linear-gradient(160deg, rgba(255,255,255,0) 0%, rgba(220,205,185,.25) 100%); }
  .person { position: relative; margin-bottom: 22px; }
  .person__name { font-size: 25px; font-weight: 400; letter-spacing: 1px; color: var(--ink); text-transform: uppercase; }
  .person__title { font-family: "Libre Baskerville", serif; font-size: 14px; letter-spacing: 2.5px; color: var(--ink-soft); margin-top: 2px; }

  .contacts { position: relative; list-style: none; }
  .contacts li { display: flex; align-items: flex-start; gap: 10px; font-size: 12px; color: var(--ink); margin-bottom: 8px; line-height: 1.3; }
  .contacts svg { width: 13px; height: 13px; flex: none; margin-top: 1px; fill: var(--ink-soft); }
</style>
</head>
<body>
  <section class="card card--front">
    <div class="pattern-fill" role="img" aria-label="Faint geometric line pattern on navy"></div>
    <div class="front-frame"></div>
    <div class="brand">
      <span class="brand__square"></span>
      <span class="brand__name">qorvil</span>
    </div>
  </section>

  <section class="card card--back">
    <div class="back-brand-panel">
      <div class="pattern-fill" role="img" aria-label="Faint geometric line pattern on navy"></div>
      <div class="brand">
        <span class="brand__square"></span>
        <span class="brand__name">qorvil</span>
      </div>
    </div>
    <div class="contact-panel">
      <div class="contact-panel__pattern" role="img" aria-label="Fine pale geometric line pattern"></div>
      <div class="person">
        <h1 class="person__name">Olena Dovbush</h1>
        <p class="person__title">Director of Marketing</p>
      </div>
      <ul class="contacts">
        <li>
          <svg viewBox="0 0 16 16"><path d="M8 1a5 5 0 0 0-5 5c0 4 5 9 5 9s5-5 5-9a5 5 0 0 0-5-5zm0 7a2 2 0 1 1 0-4 2 2 0 0 1 0 4z"/></svg>
          <span>20917 - 87 Ave. Edmonton,<br>AB, Canada. T6K 2R8</span>
        </li>
        <li>
          <svg viewBox="0 0 16 16"><path d="M1 4h14v9H1z M1 4l7 5 7-5" fill="none" stroke="#3a3a3a" stroke-width="1.6"/></svg>
          <span>helen.dovbush@mailvane.example</span>
        </li>
        <li>
          <svg viewBox="0 0 16 16"><path d="M4 1h3l1 4-2 1c1 2 2 3 4 4l1-2 4 1v3c0 1-1 2-2 2C7 14 2 9 2 3c0-1 1-2 2-2z"/></svg>
          <span>XXX.XXX.XXXX</span>
        </li>
        <li>
          <svg viewBox="0 0 16 16"><path d="M2 5c0-2 12-2 12 0v1h-3V5H5v1H2z M4 7h8l2 7H2z"/></svg>
          <span>780.555.0187</span>
        </li>
        <li>
          <svg viewBox="0 0 16 16"><circle cx="8" cy="8" r="6.5" fill="none" stroke="#3a3a3a" stroke-width="1.4"/><path d="M1.5 8h13M8 1.5c-3 3-3 10 0 13M8 1.5c3 3 3 10 0 13" fill="none" stroke="#3a3a3a" stroke-width="1.2"/></svg>
          <span>www.qorvil.example</span>
        </li>
      </ul>
    </div>
  </section>
</body>
</html>
```